dusty's business card for earthmoving and tipper hire business.

I have a small earthmoving and tipper truck company. I am aiming for the smaller jobs that the big guys don't want. I am also Doing grass slashing and fire hazard reduction work. I would like to see some earthy colors, greens browns etc. I have a tractor with a front end loader attachment, and a 22 ton tipper. I would like to maybe have a silhouette of a tipper and tractor/slasher/loader setup in centre with my business name over the top and details to one side or something like that

Industry/Entity Type

Business

Contact Information for Business Card

Dusty's small earthworks and tipper hireToowoombaABN: 47781050480PH 0479126773Email dusty.8@quarrymail-example.net

Font styles to use
Sans Serif

Colors
fbee3d
abd036
85cae6
f78f20

Requirements
Nice to have
• Earthy colors . business name in blue

```html
<!DOCTYPE html>
<html lang="en">
<head>
<meta charset="utf-8">
<title>Dusty's Earthworks and Tipper – Business Card</title>
<link href="https://fonts.googleapis.com/css2?family=Open+Sans:wght@600;700;800&display=swap" rel="stylesheet">
<style>
  :root {
    --sky: #85cae6;
    --grass: #abd036;
    --sun: #fbee3d;
    --orange: #f78f20;
    --ink: #1b1b1b;
    --night: #000000;
    --white: #ffffff;
  }
  html, body {
    margin: 0;
    padding: 0;
    overflow: hidden;
    background: var(--white);
  }
  .card {
    position: relative;
    width: 1200px;
    height: 741px;
    overflow: hidden;
    font-family: "Open Sans", Arial, sans-serif;
    background: var(--sky);
  }
  .card__landscape {
    position: absolute;
    inset: 0;
    width: 1200px;
    height: 741px;
  }
  .sky { fill: var(--sky); }
  .hill { fill: var(--grass); }
  .field { fill: var(--sun); }
  .hill-title {
    font-family: "Open Sans", Arial, sans-serif;
    font-weight: 700;
    font-size: 33px;
    fill: var(--ink);
  }
  .brand {
    position: absolute;
    left: 0;
    top: 88px;
    width: 1200px;
    margin: 0;
    text-align: center;
    font-weight: 800;
    font-size: 80px;
    line-height: 100px;
    letter-spacing: 3px;
    color: var(--white);
  }
  .brand-tagline {
    position: absolute;
    left: 0;
    top: 205px;
    width: 1200px;
    margin: 0;
    text-align: center;
    font-weight: 600;
    font-size: 24px;
    line-height: 32px;
    letter-spacing: 0.5px;
    color: var(--ink);
  }
  .fleet {
    position: absolute;
    left: 387px;
    top: 256px;
    width: 446px;
    height: 118px;
    border-radius: 10px;
    background: linear-gradient(180deg, rgba(255,255,255,0.92), rgba(255,255,255,0.78));
  }
  .services {
    position: absolute;
    left: 0;
    top: 508px;
    width: 1200px;
    margin: 0;
    padding: 0;
    text-align: center;
    color: var(--ink);
    font-weight: 600;
    font-size: 31px;
    line-height: 44px;
  }
  .services__row { display: block; }
  .services__item {
    display: inline-block;
    margin: 0 10px;
  }
  .services__item::before {
    content: "";
    display: inline-block;
    width: 11px;
    height: 11px;
    border-radius: 50%;
    background: var(--grass);
    margin-right: 11px;
    vertical-align: middle;
    position: relative;
    top: -3px;
  }
  .contact-bar {
    position: absolute;
    left: 0;
    top: 615px;
    width: 1200px;
    height: 126px;
    background: var(--night);
    color: var(--white);
    font-weight: 600;
    font-size: 24px;
  }
  .contact-bar__line {
    position: absolute;
    top: 24px;
    width: 100%;
    text-align: center;
    white-space: nowrap;
  }
  .contact-bar__sep { margin: 0 22px; }
</style>
</head>
<body>
<div class="card">
  <svg class="card__landscape" viewBox="0 0 1200 741" xmlns="http://www.w3.org/2000/svg">
    <rect class="sky" x="0" y="0" width="1200" height="741"/>
    <path class="hill" d="M0,430 Q600,350 1200,430 L1200,741 L0,741 Z"/>
    <path class="field" d="M0,510 Q600,440 1200,510 L1200,741 L0,741 Z"/>
    <defs>
      <path id="hill-arc" d="M40,482 Q600,408 1160,482"/>
    </defs>
    <text class="hill-title" text-anchor="middle">
      <textPath href="#hill-arc" startOffset="50%">Dusty's Small Earthworks &amp; Tipper Hire, Toowoomba</textPath>
    </text>
  </svg>

  <h1 class="brand">DUSTY'S</h1>
  <p class="brand-tagline">EARTHWORKS AND TIPPER</p>

  <div class="fleet" role="img" aria-label="White silhouettes of a tipper truck and a tractor with front end loader"></div>

  <p class="services">
    <span class="services__row">
      <span class="services__item">Small Earthworks</span>
      <span class="services__item">Slashing</span>
      <span class="services__item">Fire Hazard Reduction</span>
    </span>
    <span class="services__row">
      <span class="services__item">Rural Cleanups</span>
      <span class="services__item">Tipper</span>
    </span>
  </p>

  <footer class="contact-bar">
    <div class="contact-bar__line">
      <span>ABN: 36629184071</span><span class="contact-bar__sep">|</span><span>PH 0460381529</span><span class="contact-bar__sep">|</span><span>Email dusty.8@quarrymail-example.net</span>
    </div>
  </footer>
</div>
</body>
</html>
```